The Odette (wine label)

We are creating a new wine label for our vineyard in Tasmania, Australia.
This wine is dedicated to a very special person and needs to reflect elegance, beauty and longevity. We are looking for a wine label that incorporates the artwork on the attached photo (serpent tattoo).
We are calling the wine "The Odette" and it is a Pinot Noir (red wine). It is a light bodied but elegant wine, which reflects the person that it is named after.
The wine will be a 2024 Vintage Pinot Noir.

```html
<!DOCTYPE html>
<html lang="en">
<head>
<meta charset="UTF-8">
<title>The Odette — Pinot Noir Label</title>
<link rel="stylesheet" href="https://fonts.googleapis.com/css2?family=Cormorant+Garamond:wght@500&family=Mrs+Saint+Delafield&display=swap">
<style>
  :root {
    --backdrop: #1d1b1a;
    --label-paper: #f6f2f1;
    --gold: #c9a043;
    --gold-light: #e6cd8a;
    --ink: #151312;
  }
  * { margin: 0; padding: 0; box-sizing: border-box; }
  html, body {
    width: 1200px;
    height: 800px;
    overflow: hidden;
    background: var(--backdrop);
  }
  .canvas {
    width: 1200px;
    height: 800px;
    display: flex;
    align-items: center;
    justify-content: center;
  }
  .wine-label {
    position: relative;
    width: 800px;
    height: 660px;
    background: var(--label-paper);
  }
  .gold-frame {
    position: absolute;
    inset: 30px;
    border: 4px solid var(--gold);
  }
  .serpent-artwork {
    position: absolute;
    left: 48px;
    top: 48px;
    width: 650px;
    height: 370px;
    border-radius: 180px 200px 160px 220px;
    background: radial-gradient(ellipse at 45% 50%, rgba(216,181,104,0.45), rgba(216,181,104,0.12) 65%, rgba(246,242,241,0) 80%);
  }
  .wine-name {
    position: absolute;
    left: 0;
    right: 0;
    top: 360px;
    padding-left: 110px;
    text-align: center;
    font-family: "Mrs Saint Delafield", cursive;
    font-size: 112px;
    line-height: 1;
    color: var(--ink);
  }
  .varietal {
    position: absolute;
    left: 0;
    right: 0;
    top: 512px;
    padding-left: 60px;
    text-align: center;
    font-family: "Cormorant Garamond", serif;
    font-weight: 500;
    font-size: 30px;
    letter-spacing: 2px;
    text-transform: uppercase;
    color: var(--ink);
  }
  .origin-vintage {
    position: absolute;
    left: 0;
    right: 0;
    top: 560px;
    padding-left: 60px;
    text-align: center;
    font-family: "Cormorant Garamond", serif;
    font-weight: 500;
    font-size: 17px;
    letter-spacing: 1px;
    text-transform: uppercase;
    color: var(--ink);
  }
</style>
</head>
<body>
  <main class="canvas">
    <section class="wine-label">
      <div class="gold-frame"></div>
      <div class="serpent-artwork" role="img" aria-label="Gold line illustration of a coiled serpent with scaled body winding across the top of the label"></div>
      <h1 class="wine-name">The Odette</h1>
      <p class="varietal">Pinot Noir</p>
      <p class="origin-vintage">Tasmania, Australia / 2024</p>
    </section>
  </main>
</body>
</html>
```